Banner for my Adult Tube Site

Hi,
i need 5 animated banner .gif for my Adult Tube Site https://velvorinstream.example
N.2 300x250
N.2 728x90
N.1 160x600
You can add image in the banner only with  free copyright.
I leave you to think about something that attracts attention to being clicked.

```html
<!DOCTYPE html>
<html lang="en">
<head>
<meta charset="UTF-8">
<title>Velvorin Stream Banner</title>
<link rel="stylesheet" href="https://fonts.googleapis.com/css2?family=Open+Sans:wght@500&display=swap">
<style>
  :root {
    --frame-pink: #ff3b6b;
    --panel-dark: #1b1b1b;
    --glow-pink: #ff6fa0;
    --glow-white: #ffe9f1;
    --text-light: #fff5f8;
    --spark-red: #c0294a;
  }
  html, body {
    margin: 0;
    padding: 0;
    width: 1200px;
    height: 148px;
    overflow: hidden;
    background: var(--frame-pink);
  }
  .banner {
    position: relative;
    width: 1200px;
    height: 148px;
    box-sizing: border-box;
    background: var(--frame-pink);
  }
  .banner-panel {
    position: absolute;
    left: 13px;
    top: 10px;
    width: 1174px;
    height: 128px;
    background: var(--panel-dark);
    overflow: hidden;
  }
  .edge-glow {
    position: absolute;
    left: 50%;
    width: 260px;
    height: 14px;
    transform: translateX(-50%);
    border-radius: 50%;
    background: radial-gradient(ellipse at center, var(--glow-white) 0%, var(--glow-pink) 45%, rgba(255,59,107,0) 75%);
  }
  .edge-glow--top { top: -7px; }
  .edge-glow--bottom { bottom: -7px; }
  .sparks {
    position: absolute;
    inset: 0;
  }
  .cta-label {
    position: absolute;
    left: 240px;
    top: 58px;
    margin: 0;
    font-family: "Open Sans", sans-serif;
    font-weight: 500;
    font-size: 42px;
    letter-spacing: 1px;
    line-height: 1;
    color: var(--text-light);
    text-shadow: 0 0 4px var(--glow-pink), 0 0 10px var(--frame-pink), 0 0 18px var(--frame-pink);
  }
</style>
</head>
<body>
  <a class="banner" href="https://velvorinstream.example" aria-label="velvorinstream.example" style="display:block;text-decoration:none;">
    <div class="banner-panel">
      <span class="edge-glow edge-glow--top"></span>
      <span class="edge-glow edge-glow--bottom"></span>
      <svg class="sparks" width="1174" height="128" aria-hidden="true">
        <circle cx="150" cy="35" r="1.5" fill="var(--spark-red)"/>
        <circle cx="67" cy="62" r="1.2" fill="var(--spark-red)"/>
        <circle cx="128" cy="95" r="1.2" fill="var(--spark-red)"/>
        <circle cx="600" cy="35" r="1.5" fill="var(--spark-red)"/>
        <circle cx="578" cy="95" r="1.3" fill="var(--spark-red)"/>
        <circle cx="410" cy="22" r="1" fill="var(--spark-red)"/>
      </svg>
      <p class="cta-label">CLICK HERE</p>
    </div>
  </a>
</body>
</html>
```